Belford & Company

We are a boutique commercial real estate firm. For our Business card design - sleek, modern, yet high-end/classy. Please see our website: belfordandcompany.example for details.

We currently need 2 business card names and the ability to add/change the business card information -
Name, Title, Address, Office #, Mobile #, Fax, Email and company website.

Industry/Entity Type

Real Estate

Contact Information for Business Card

Business card design - sleek, modern, yet high-end/classy. Please see our website: belfordandcompany.example for details.

Also, we'd like to have our slogan "Precision Sets The Standard." somewhere in there. We'd like to make some part of it raised or a different texture if possible.
Color #'s:
blue 19 36 128
light gray 222 222 221
dark gray 107 120 128

Also, we'd like to have our slogan "Precision Sets The Standard." somewhere in there. We'd like to make some part of it raised or a different texture if possible - grey on one side and blue on the other - rounded edges preferred. Maybe either metal/silver/grey raised logo on the back. Thank you!!

Requirements
Must have
• Sleek, modern, clean and classy design

```html
<!DOCTYPE html>
<html lang="en">
<head>
<meta charset="utf-8">
<title>Belford &amp; Company – Business Card</title>
<link href="https://fonts.googleapis.com/css2?family=Oswald:wght@400;500&family=Montserrat:wght@400;700&family=Raleway:wght@400&display=swap" rel="stylesheet">
<style>
  :root {
    --brand-blue: #21469b;
    --name-blue: #1f3e9c;
    --slate: #6b7880;
    --panel-slate: #75868f;
    --line-slate: #8a979e;
    --paper: #ffffff;
    --backdrop: #cccccc;
  }
  * { box-sizing: border-box; margin: 0; padding: 0; }
  html, body { width: 1200px; height: 1200px; overflow: hidden; }
  body { background: var(--backdrop); position: relative; }

  .card {
    position: absolute; top: 250px;
    width: 410px; height: 700px;
    border-radius: 48px; overflow: hidden;
  }

  /* Back side */
  .card-back { left: 188px; background: var(--brand-blue); }
  .card-back .logo-frame {
    position: absolute; left: 70px; top: 276px; width: 274px; height: 152px;
    border: 2px solid var(--line-slate);
    display: flex; align-items: center; justify-content: center; gap: 12px;
  }
  .logo-mark { width: 20px; height: 20px; background: var(--line-slate); flex: none; }
  .logo-name {
    font-family: "Oswald", sans-serif; font-weight: 500; color: #fff;
    font-size: 30px; line-height: 1.05; text-transform: uppercase; letter-spacing: .5px;
  }
  .web-band {
    position: absolute; left: 0; top: 539px; width: 360px; height: 34px;
    background: var(--panel-slate);
    font-family: "Montserrat", sans-serif; font-size: 16px; color: #fff;
    display: flex; align-items: center; justify-content: flex-end; padding-right: 14px;
    letter-spacing: .3px; white-space: nowrap;
  }

  /* Front side */
  .card-front { left: 602px; background: var(--paper); }
  .card-front .logo-box {
    position: absolute; left: 89px; top: 36px; width: 230px; height: 127px;
    background: var(--brand-blue); border: 2px solid var(--line-slate);
    display: flex; align-items: center; justify-content: center; gap: 10px;
  }
  .card-front .logo-name { font-size: 26px; }
  .tagline {
    position: absolute; left: 0; width: 100%; top: 212px; text-align: center;
    font-family: "Oswald", sans-serif; font-weight: 400; font-size: 32px;
    color: var(--slate); transform: scaleX(.88); white-space: nowrap;
  }
  .rule { position: absolute; height: 2px; background: var(--line-slate); }
  .rule-top { left: 91px; right: 0; top: 316px; }
  .rule-bottom { left: 0; width: 317px; top: 388px; }
  .person { position: absolute; left: 0; width: 410px; top: 320px; text-align: center; }
  .person-name {
    font-family: "Montserrat", sans-serif; font-weight: 700; font-size: 28px;
    color: var(--name-blue); line-height: 1.2;
  }
  .person-title {
    font-family: "Montserrat", sans-serif; font-size: 19px; color: var(--slate);
    letter-spacing: .5px;
  }
  .contact-panel {
    position: absolute; left: 43px; width: 324px; top: 445px; bottom: 0;
    background: var(--panel-slate); border-radius: 36px 36px 0 0;
    font-family: "Raleway", sans-serif; color: #fff; font-size: 17px;
    text-align: center; padding: 18px 10px 0;
  }
  .address { margin-bottom: 28px; white-space: nowrap; }
  .contact-list {
    list-style: none; display: flex; flex-direction: column; align-items: center; gap: 6px;
    font-size: 15px;
  }
  .contact-list li { display: flex; align-items: center; gap: 5px; line-height: 22px; white-space: nowrap; }
  .contact-list svg { width: 14px; height: 14px; fill: #fff; flex: none; }
</style>
</head>
<body>

<section class="card card-back" aria-label="Business card back">
  <div class="logo-frame">
    <span class="logo-mark"></span>
    <span class="logo-name">Belford<br>&amp; Company</span>
  </div>
  <div class="web-band">www.belfordandcompany.example</div>
</section>

<section class="card card-front" aria-label="Business card front">
  <div class="logo-box">
    <span class="logo-mark"></span>
    <span class="logo-name">Belford<br>&amp; Company</span>
  </div>
  <p class="tagline">Precision Sets The Standard</p>
  <div class="rule rule-top"></div>
  <div class="person">
    <p class="person-name">Your Full Name</p>
    <p class="person-title">Founder / President</p>
  </div>
  <div class="rule rule-bottom"></div>
  <div class="contact-panel">
    <p class="address">Your Full Address Comes here</p>
    <ul class="contact-list">
      <li><svg viewBox="0 0 16 16"><path d="M3 1l3 3-1.5 2a9 9 0 0 0 5.5 5.5L12 10l3 3-2 2C7 15 1 9 1 3z"/></svg>: 000 000 0000</li>
      <li><svg viewBox="0 0 16 16"><path d="M4 0h8v16H4zM5.5 2v10h5V2zM7 13h2v1.5H7z" fill-rule="evenodd"/></svg>: 000 000 0000</li>
      <li><svg viewBox="0 0 16 16"><path d="M4 1h8v4H4zM1 6h14v6h-3v3H4v-3H1zM5 10v4h6v-4z" fill-rule="evenodd"/></svg>: 000 000 0000</li>
      <li><svg viewBox="0 0 16 16"><path d="M0 3h16v10H0zM1.5 4.5L8 9l6.5-4.5V12h-13z" fill-rule="evenodd"/></svg>: info@belfordandcompany.example</li>
    </ul>
  </div>
</section>

</body>
</html>
```